Harbor Flow Plumbing Requires Head Turning Truck Wrap Design

We need a head turning, eye catching, standout wrap design for our company vehicles. Our original got the job done but it's time to upgrade. It needs to be sleek, modern and emphasize professionalism. We are a premium brand built on exceptional service and lasting client relationships. Please done include any design on the black cap at the rear of the truck, it should only be on the actual truck itself.

Target Market(s)

Everyone

Industry/Entity Type

Plumbing

Colors
0054AA
0677BA
7BADD7
CADEEF
E8F1F8

Requirements
Should not have
• Cartoon Characters, Cartoon Looking Design, Any Design on the Truck Bed Cap.

```html
<!DOCTYPE html>
<html lang="en">
<head>
<meta charset="utf-8">
<title>Harbor Flow Plumbing – Vehicle Wrap</title>
<link rel="stylesheet" href="https://fonts.googleapis.com/css2?family=Poppins:ital,wght@0,500;0,600;0,700;1,700&family=Oswald:wght@600&display=swap">
<style>
  :root {
    --navy: #0054AA;
    --ocean: #0677BA;
    --sky: #1fa3dc;
    --bright: #0aa6e6;
    --mist: #7BADD7;
    --ice: #CADEEF;
    --foam: #E8F1F8;
    --white: #ffffff;
  }
  * { margin: 0; padding: 0; box-sizing: border-box; }
  html, body { width: 1200px; height: 795px; overflow: hidden; background: var(--white); }
  .canvas { position: relative; width: 1200px; height: 795px; background: var(--white); }
  .wrap-panel {
    position: absolute; left: 65px; top: 212px; width: 1070px; height: 331px;
    overflow: hidden; font-family: "Poppins", sans-serif; color: var(--white);
  }
  .water-art {
    position: absolute; inset: 0;
    background:
      radial-gradient(ellipse 60% 40% at 30% 60%, rgba(202,222,239,.45), transparent 70%),
      linear-gradient(180deg, #1e8fd0 0%, #2aa9e0 45%, #1b86cc 75%, #1f9ad8 100%);
  }
  .bands { position: absolute; inset: 0; }
  .brand { position: absolute; left: 286px; top: 150px; width: 232px; text-align: center; }
  .brand-name { font-weight: 700; font-size: 66px; line-height: 1; letter-spacing: 2px; }
  .brand-rule { height: 2px; background: var(--white); margin: 8px 0 5px; }
  .brand-full { font-weight: 500; font-size: 12.5px; letter-spacing: .2px; }
  .brand-phone { margin-top: 6px; font-weight: 600; font-size: 16px; display: flex; align-items: center; justify-content: center; gap: 6px; }
  .brand-phone svg { width: 15px; height: 15px; }
  .web-address {
    position: absolute; left: 614px; top: 140px; transform: translate(-50%, -50%) rotate(-64deg);
    font-weight: 700; font-size: 27px; color: var(--ice); white-space: nowrap; opacity: .9;
  }
  .services { position: absolute; left: 0; top: 0; list-style: none; }
  .services li {
    position: absolute; white-space: nowrap; font-weight: 700; font-style: italic; font-size: 16px;
    display: flex; align-items: center; gap: 7px;
  }
  .services li::before {
    content: ""; width: 7px; height: 7px; border-radius: 50%; border: 1.5px solid var(--white); background: var(--mist);
  }
  .tagline {
    position: absolute; left: 686px; top: 107px; width: 242px; text-align: center;
    font-family: "Oswald", sans-serif; font-weight: 600; font-size: 22px; line-height: 27px;
    border-top: 1px solid var(--ice); border-bottom: 1px solid var(--ice); padding: 4px 0;
  }
  .emergency { position: absolute; left: 632px; top: 188px; width: 130px; text-align: center; }
  .emergency-hours { font-weight: 600; font-size: 38px; line-height: 44px; }
  .emergency-label { font-weight: 700; font-size: 14px; line-height: 16px; }
  .emergency-rule { position: absolute; left: 672px; top: 232px; width: 90px; height: 1px; background: var(--ice); opacity: .6; }
  .brand-mark-large {
    position: absolute; left: 972px; top: 128px; transform: translate(-50%, -50%) rotate(-64deg);
    font-weight: 700; font-size: 92px; line-height: 1; letter-spacing: 4px; color: var(--white); white-space: nowrap;
  }
  .licences { position: absolute; left: 928px; top: 215px; width: 120px; text-align: center; font-weight: 700; }
  .licences .licence-ph { font-size: 10.5px; }
  .licences .licence-tssa { font-size: 8px; }
</style>
</head>
<body>
<div class="canvas">
  <section class="wrap-panel">
    <div class="water-art" role="img" aria-label="Flowing blue water wave with bubbles across the panel"></div>
    <svg class="bands" viewBox="0 0 1070 331" preserveAspectRatio="none" aria-hidden="true">
      <polygon points="570,331 730,0 1070,0 1070,331" fill="var(--navy)" opacity=".88"/>
      <polygon points="549,331 711,0 742,0 580,331" fill="var(--mist)" opacity=".75"/>
      <polygon points="840,331 1001,0 1070,0 1070,331" fill="var(--bright)"/>
      <polygon points="822,331 983,0 1001,0 840,331" fill="var(--sky)" opacity=".8"/>
    </svg>

    <div class="brand">
      <div class="brand-name">HFP</div>
      <div class="brand-rule"></div>
      <div class="brand-full">HARBOR FLOW PLUMBING</div>
      <div class="brand-phone">
        <svg viewBox="0 0 24 24" fill="var(--white)" aria-hidden="true"><path d="M6.6 10.8a15.1 15.1 0 0 0 6.6 6.6l2.2-2.2a1 1 0 0 1 1-.25 11.4 11.4 0 0 0 3.6.57 1 1 0 0 1 1 1V20a1 1 0 0 1-1 1A17 17 0 0 1 3 4a1 1 0 0 1 1-1h3.5a1 1 0 0 1 1 1c0 1.25.2 2.45.57 3.6a1 1 0 0 1-.25 1z"/></svg>
        833-555-0142
      </div>
    </div>

    <div class="web-address">www.hfp.works</div>

    <ul class="services">
      <li style="left:720px;top:30px">PLUMBING REPAIRS</li>
      <li style="left:709px;top:55px">DRAIN CLEANING</li>
      <li style="left:697px;top:80px">WATER HEATERS</li>
    </ul>

    <div class="tagline">PROFESSIONAL SERVICES<br>IS OUR STANDARD</div>

    <div class="emergency">
      <div class="emergency-hours">24/7</div>
      <div class="emergency-label">EMERGENCY<br>SERVICE</div>
    </div>

    <div class="brand-mark-large">HFP</div>

    <div class="licences">
      <div class="licence-ph">PH41257</div>
      <div class="licence-tssa">TSSA 0000512846017</div>
    </div>
  </section>
</div>
</body>
</html>
```